Ridgeline Build Network Inc. Letterhead

Creation of attractive and eye catching letterhead for a business start-up for the construction industry. Letterhead must relate to construction, but avoid standard hammer and tools in the design.
Updates

I forgot to add some details, sorry about that. Some pertinent info: Ph: 555-555-0148 ridgelinebuildnet.example 487 Willowmere Ave, Ste 210 Folsom, CA 95699 info@ridgelinebuildnet.example not sure if slogan should be in there" “Connecting construction professionals to create a purpose driven industry.” must be able to be used in word. Thanks!

```html
<!DOCTYPE html>
<html lang="en">
<head>
<meta charset="utf-8">
<title>Ridgeline Build Network Inc. – Letterhead</title>
<link rel="stylesheet" href="https://fonts.googleapis.com/css2?family=Questrial&family=Montserrat:wght@600&family=Open+Sans:wght@700&family=Tinos&display=swap">
<style>
  :root {
    --board: #ebe3e3;
    --navy: #1b1f4e;
    --red: #b91f26;
    --white: #ffffff;
    --label: #333333;
    --faint: rgba(27, 31, 78, 0.12);
  }
  * { box-sizing: border-box; margin: 0; padding: 0; }
  html, body { width: 1200px; height: 873px; overflow: hidden; }
  body { background: var(--board); position: relative; font-family: "Questrial", sans-serif; }

  .board-label {
    position: absolute;
    font-family: "Open Sans", sans-serif;
    font-weight: 700;
    color: var(--label);
    text-align: center;
    line-height: 1;
  }
  .board-label--option { left: 0; width: 1234px; top: 28px; font-size: 62px; }
  .board-label--front  { left: 103px; width: 469px; top: 780px; font-size: 52px; }
  .board-label--back   { left: 614px; width: 469px; top: 780px; font-size: 52px; }

  .sheet {
    position: absolute;
    top: 142px;
    width: 469px;
    height: 606px;
    box-shadow: 0 2px 8px rgba(0, 0, 0, 0.25);
  }
  .sheet--front { left: 103px; background: var(--white); }
  .sheet--back  { left: 614px; background: var(--navy); }

  .sidebar { position: absolute; left: 0; top: 0; width: 195px; height: 606px; }
  .sidebar svg { display: block; }

  .brand {
    position: absolute;
    left: 0; width: 195px; top: 174px;
    text-align: center;
    font-family: "Montserrat", sans-serif;
    font-weight: 600;
    color: var(--white);
    font-size: 15px;
    letter-spacing: 1.5px;
    line-height: 1.35;
    text-transform: uppercase;
  }
  .brand-mark {
    display: block;
    width: 22px; height: 22px;
    margin: 0 auto 12px;
    background: var(--red);
  }

  .contact {
    position: absolute;
    left: 20px; top: 474px;
    list-style: none;
    font-family: "Tinos", serif;
    color: var(--white);
    font-size: 11.5px;
    line-height: 1.2;
  }
  .contact li { display: flex; align-items: flex-start; gap: 6px; margin-bottom: 4px; }
  .contact svg { flex: none; width: 10px; height: 10px; margin-top: 2px; }

  .slogan {
    position: absolute;
    left: 195px; width: 274px; top: 20px;
    text-align: center;
  }
  .slogan-lead { color: var(--red); font-size: 26px; line-height: 1.05; }
  .slogan-main { color: var(--navy); font-size: 20px; line-height: 1.2; }
  .slogan-sub  { color: var(--navy); font-size: 14px; line-height: 1.2; }

  .watermark {
    position: absolute;
    left: 195px; width: 274px; top: 508px;
    text-align: center;
    font-family: "Montserrat", sans-serif;
    font-weight: 600;
    color: var(--faint);
    font-size: 13px;
    letter-spacing: 1.5px;
    line-height: 1.35;
    text-transform: uppercase;
  }

  .back-brand {
    position: absolute;
    left: 0; width: 469px; top: 232px;
    text-align: center;
    font-family: "Montserrat", sans-serif;
    font-weight: 600;
    color: var(--white);
    font-size: 27px;
    letter-spacing: 3px;
    line-height: 1.35;
    text-transform: uppercase;
  }
  .back-brand .brand-mark { width: 34px; height: 34px; margin-bottom: 22px; background: var(--white); }
</style>
</head>
<body>
  <div class="board-label board-label--option">OPTION 02</div>

  <section class="sheet sheet--front">
    <div class="sidebar">
      <svg width="195" height="606" viewBox="0 0 195 606" aria-hidden="true">
        <rect width="195" height="606" fill="var(--navy)"/>
        <polygon points="0,404 94,436 195,404 195,606 0,606" fill="var(--white)"/>
        <polygon points="0,414 94,446 195,414 195,606 0,606" fill="var(--red)"/>
      </svg>
    </div>

    <div class="brand"><span class="brand-mark"></span>Ridgeline Build<br>Network Inc.</div>

    <ul class="contact">
      <li>
        <svg viewBox="0 0 10 10" aria-hidden="true"><path d="M2 1h2l1 2.5-1.3 1a5 5 0 0 0 2 2l1-1.3L9 6.3v2L8 9C4 9 1 6 1 2z" fill="var(--white)"/></svg>
        555-555-0148
      </li>
      <li>
        <svg viewBox="0 0 10 10" aria-hidden="true"><circle cx="5" cy="5" r="4" fill="none" stroke="var(--white)" stroke-width="1"/><path d="M1 5h8M5 1c-2 2-2 6 0 8M5 1c2 2 2 6 0 8" fill="none" stroke="var(--white)" stroke-width="0.7"/></svg>
        ridgelinebuildnet.example
      </li>
      <li>
        <svg viewBox="0 0 10 10" aria-hidden="true"><rect x="0.5" y="2" width="9" height="6" fill="var(--white)"/><path d="M0.5 2l4.5 3.5L9.5 2" fill="none" stroke="var(--red)" stroke-width="0.8"/></svg>
        info@ridgelinebuildnet.example
      </li>
      <li>
        <svg viewBox="0 0 10 10" aria-hidden="true"><path d="M5 0.5a3 3 0 0 1 3 3c0 2.3-3 6-3 6s-3-3.7-3-6a3 3 0 0 1 3-3z" fill="var(--white)"/><circle cx="5" cy="3.5" r="1.1" fill="var(--red)"/></svg>
        <span>487 Willowmere Ave, Ste 210<br>Maplecrest WA 95699</span>
      </li>
    </ul>

    <div class="slogan">
      <div class="slogan-lead">Connecting</div>
      <div class="slogan-main">Construction Professionals</div>
      <div class="slogan-sub">To Create a Purpose Driven Industry.</div>
    </div>

    <div class="watermark">Ridgeline Build<br>Network Inc.</div>
  </section>

  <section class="sheet sheet--back">
    <div class="back-brand"><span class="brand-mark"></span>Ridgeline Build<br>Network Inc.</div>
  </section>

  <div class="board-label board-label--front">FRONT</div>
  <div class="board-label board-label--back">BACK</div>
</body>
</html>
```